BrimstoneHoldingsLLC

Real Estate Investment. Buy/Sell house/investment . Trustworthy,Reliable, and friendly

Industry/Entity Type

Real Estate

Contact Information for Business Card

BrimstoneHoldings@mailtrove.com
555-413-2960
Tamsin-Leigh Okafor

```html
<!DOCTYPE html>
<html lang="en">
<head>
<meta charset="utf-8">
<title>Brimstone Holdings LLC – Business Card</title>
<link rel="stylesheet" href="https://fonts.googleapis.com/css2?family=Cinzel:wght@500&family=Tinos&display=swap">
<style>
  :root {
    --backdrop: #2b2b2b;
    --paper: #f3f4f5;
    --slate-blue: #3f5b73;
    --brand-ink: #2a2e33;
    --card-text: #f2f4f6;
  }
  html, body {
    margin: 0;
    padding: 0;
    width: 1200px;
    height: 900px;
    overflow: hidden;
    background: var(--backdrop);
  }
  .canvas {
    position: relative;
    width: 1200px;
    height: 900px;
  }
  .business-card {
    position: absolute;
    left: 300px;
    top: 70px;
    width: 840px;
    height: 480px;
    display: flex;
    box-shadow: 0 10px 30px rgba(0,0,0,0.45);
  }
  .card-front {
    flex: 0 0 55%;
    background: var(--paper);
    display: flex;
    align-items: center;
    justify-content: center;
  }
  .card-back {
    flex: 1;
    min-width: 0;
    background: var(--slate-blue);
    color: var(--card-text);
    font-family: "Tinos", "Times New Roman", serif;
    padding: 130px 28px 0 36px;
    box-sizing: border-box;
  }
  .brand-name {
    font-family: "Cinzel", "Trajan Pro", serif;
    font-weight: 500;
    color: var(--brand-ink);
    text-align: center;
    line-height: 1.15;
    margin: 0;
  }
  .card-front .brand-name { font-size: 44px; }
  .holder-name {
    font-size: 26px;
    margin: 0 0 40px;
    white-space: nowrap;
  }
  .contact-line {
    font-size: 19px;
    margin: 0 0 6px;
    white-space: nowrap;
  }
  .logo-sheet {
    position: absolute;
    left: 10px;
    top: 592px;
    width: 448px;
    height: 298px;
    background: #ffffff;
    display: flex;
    align-items: center;
    justify-content: center;
  }
  .logo-sheet .brand-name { font-size: 38px; }
</style>
</head>
<body>
<main class="canvas">
  <section class="business-card">
    <div class="card-front">
      <p class="brand-name">Brimstone<br>Holdings LLC</p>
    </div>
    <div class="card-back">
      <p class="holder-name">Tamsin-Leigh Okafor</p>
      <p class="contact-line">555-413-2960</p>
      <p class="contact-line">BrimstoneHoldings@mailtrove.com</p>
    </div>
  </section>
  <section class="logo-sheet">
    <p class="brand-name">Brimstone<br>Holdings LLC</p>
  </section>
</main>
</body>
</html>
```